Business Card Design - Local Discount Club

Looking for a fun business card for a local discount club. One side should be the logo only and the other should be have :

Name
Title
Phone, Email
Website

```html
<!DOCTYPE html>
<html lang="en">
<head>
<meta charset="utf-8">
<title>The Harbor Pass – Business Card</title>
<link href="https://fonts.googleapis.com/css2?family=Open+Sans:wght@400;600;700&display=swap" rel="stylesheet">
<style>
  :root {
    --page-bg: #d9dadc;
    --card-bg: #ffffff;
    --brand-navy: #2f4f9e;
    --brand-sky: #4cb4e2;
    --brand-lime: #8cc152;
    --text-dark: #2b2b2b;
    --divider: #9aa4c4;
  }
  * { box-sizing: border-box; margin: 0; padding: 0; }
  html, body {
    width: 1200px; height: 900px; overflow: hidden;
    background: var(--page-bg);
    font-family: "Open Sans", Arial, sans-serif;
  }
  .canvas {
    width: 1200px; height: 900px;
    display: flex; flex-direction: column; align-items: center; justify-content: center;
    gap: 48px;
  }
  .card {
    position: relative;
    width: 640px; height: 366px;
    background: var(--card-bg);
    border-radius: 28px;
    box-shadow: 0 10px 28px rgba(0,0,0,0.18);
  }
  .brand {
    display: flex; align-items: center; gap: 12px;
    color: var(--brand-navy);
    font-weight: 700;
    white-space: nowrap;
  }
  .brand-dot {
    border-radius: 50%;
    background: var(--brand-sky);
    flex: none;
  }
  .card-front .brand {
    position: absolute; left: 50%; top: 50%;
    transform: translate(-50%, -50%);
    font-size: 40px;
  }
  .card-front .brand-dot { width: 18px; height: 18px; }
  .card-back .brand {
    position: absolute; left: 48px; top: 52px;
    font-size: 34px;
  }
  .card-back .brand-dot { width: 15px; height: 15px; }
  .details {
    position: absolute; left: 0; right: 40px; bottom: 64px;
    display: flex; justify-content: flex-end; align-items: center;
  }
  .person {
    text-align: right;
    padding-right: 18px;
  }
  .person-title {
    font-size: 18px; color: var(--text-dark); line-height: 1.2;
  }
  .person-name {
    font-size: 22px; font-weight: 700; color: var(--brand-sky);
    letter-spacing: 0.5px; line-height: 1.2;
  }
  .contact-list {
    list-style: none;
    border-left: 1.5px solid var(--divider);
    padding-left: 16px;
    display: flex; flex-direction: column; gap: 8px;
  }
  .contact-item {
    display: flex; align-items: center; gap: 10px;
    font-size: 17px; color: var(--text-dark);
  }
  .contact-icon { width: 18px; height: 18px; flex: none; }
</style>
</head>
<body>
<main class="canvas">
  <section class="card card-front" aria-label="Card front">
    <div class="brand"><span class="brand-dot"></span>The Harbor Pass</div>
  </section>

  <section class="card card-back" aria-label="Card back">
    <div class="brand"><span class="brand-dot"></span>The Harbor Pass</div>
    <div class="details">
      <div class="person">
        <p class="person-title">Director</p>
        <p class="person-name">ELLIS HART</p>
      </div>
      <ul class="contact-list">
        <li class="contact-item">
          <svg class="contact-icon" viewBox="0 0 24 24" aria-hidden="true"><path fill="#4cb4e2" d="M6.6 10.8a15.1 15.1 0 0 0 6.6 6.6l2.2-2.2c.3-.3.7-.4 1-.2 1.1.4 2.3.6 3.6.6.6 0 1 .4 1 1V20c0 .6-.4 1-1 1A17 17 0 0 1 3 4c0-.6.4-1 1-1h3.5c.6 0 1 .4 1 1 0 1.3.2 2.5.6 3.6.1.3 0 .7-.2 1z"/></svg>
          555-014-2278
        </li>
        <li class="contact-item">
          <svg class="contact-icon" viewBox="0 0 24 24" aria-hidden="true"><rect x="2" y="5" width="20" height="14" rx="2" fill="#4cb4e2"/><path d="M3 6.5l9 6.5 9-6.5" fill="none" stroke="#fff" stroke-width="1.6"/></svg>
          hello@harborpassclub.com
        </li>
        <li class="contact-item">
          <svg class="contact-icon" viewBox="0 0 24 24" aria-hidden="true"><g fill="none" stroke="#4cb4e2" stroke-width="1.8"><circle cx="12" cy="12" r="9"/><ellipse cx="12" cy="12" rx="4" ry="9"/><path d="M3 12h18"/></g></svg>
          www.harborpassclub.com
        </li>
      </ul>
    </div>
  </section>
</main>
</body>
</html>
```